Financial Services Consultant needs a business card

We need a business card for a new consulting company based in Melbourne called
"Qorvel Insights". Tagline is Measure, Monitor, Save
We would like to see business card designs that are in line with the minimal style of the website www.qorvel-insights.example
The font I have used on the website is Proxima Nova and would like the same or similar font used on the business card with a minimal design in line with the website Two sided with "QORVEL INSIGHTS" MEASURE, MONITOR, SAVE on one side and name, title and contact details on the otther
Updates

Hi All, thanks for your submissions, much appreciated.

I have recently added some colour to my webiste, it is hex #3a7b74 for those that wish to use it
Thanks

Hi all

thanks very much for your design submissions I am very impressed and they are much appreciated.

Interms of general feedback please find below;

Colour: I am trying to stick to a minimal design and colour scheme for my website which is still under construction, up to 3 colours( www.qorvel-insights.example) it is currently black and white with a small amount of blue/green but I am open to suggestion/interpretations for a consulting company.

Card: I dont mind if it has rounded edges or straight, I was thinking about using a letterpress card if possible

Detail: the detail on the card will include; Name, Title, Mobile, Personal Email, Business Email,Web,Business Address

Once again thanks for submissions

Industry/Entity Type

Business

```html
<!DOCTYPE html>
<html lang="en">
<head>
<meta charset="utf-8">
<title>Qorvel Insights — Business Card</title>
<link rel="stylesheet" href="https://fonts.googleapis.com/css2?family=Montserrat:wght@400;500;600;700&display=swap">
<style>
  :root {
    --page-bg: #f4f4f4;
    --card-bg: #ffffff;
    --ink: #000000;
    --teal: #3a7b74;
    --faint: #ececec;
    --rule: #e2e2e2;
    --edge-light: #bdbdbd;
    --edge-dark: #2a2a2a;
  }
  * { box-sizing: border-box; margin: 0; padding: 0; }
  html, body {
    width: 1200px;
    height: 383px;
    overflow: hidden;
    background: var(--page-bg);
    font-family: "Montserrat", Arial, sans-serif;
    color: var(--ink);
  }
  .canvas {
    position: relative;
    width: 1200px;
    height: 383px;
  }
  .card {
    position: absolute;
    top: 14px;
    width: 564px;
    height: 357px;
    background: var(--card-bg);
    overflow: hidden;
  }

  /* Front side */
  .card--front {
    left: 16px;
    border: 1px solid var(--edge-light);
    box-shadow: 1px 2px 3px rgba(0, 0, 0, 0.18);
    text-align: center;
  }
  .front__name {
    position: absolute;
    left: 0;
    right: 0;
    top: 136px;
    font-size: 44px;
    font-weight: 400;
    letter-spacing: 1.5px;
    line-height: 1;
  }
  .front__tagline {
    position: absolute;
    left: 0;
    right: 0;
    top: 210px;
    font-size: 11.5px;
    font-weight: 600;
    letter-spacing: 0.8px;
    color: var(--teal);
  }

  /* Back side */
  .card--back {
    left: 625px;
    border: 1px solid var(--edge-dark);
  }
  .back__header {
    position: absolute;
    left: 0;
    top: 0;
    width: 100%;
    height: 198px;
    border-bottom: 1px solid var(--rule);
  }
  .back__brand {
    position: absolute;
    right: 22px;
    top: 76px;
    display: flex;
    align-items: center;
    gap: 12px;
    font-size: 38px;
    font-weight: 400;
    color: var(--faint);
    line-height: 1;
  }
  .back__brand-mark {
    width: 26px;
    height: 26px;
    background: var(--faint);
  }
  .contact {
    position: absolute;
    left: 318px;
    top: 225px;
    line-height: 1.2;
  }
  .contact__name {
    font-size: 16.5px;
    font-weight: 500;
    letter-spacing: 0.3px;
    margin-bottom: 2px;
  }
  .contact__line {
    font-size: 13px;
    font-weight: 500;
  }
  .back__footer {
    position: absolute;
    left: 0;
    bottom: 0;
    width: 100%;
    height: 29px;
    background: var(--teal);
    color: var(--card-bg);
    font-size: 13.5px;
    font-weight: 500;
    text-align: center;
    line-height: 29px;
  }
</style>
</head>
<body>
  <main class="canvas">
    <section class="card card--front" aria-label="Business card front">
      <h1 class="front__name">QORVEL INSIGHTS</h1>
      <p class="front__tagline">MEASURE , MONITOR , SAVE</p>
    </section>

    <section class="card card--back" aria-label="Business card back">
      <div class="back__header">
        <div class="back__brand">
          <span class="back__brand-mark" aria-hidden="true"></span>
          <span>Qorvel Insights</span>
        </div>
      </div>
      <div class="contact">
        <p class="contact__name">FIRST NAME LAST NAME</p>
        <p class="contact__line">TITLE</p>
        <p class="contact__line">Address goes here</p>
        <p class="contact__line">+61-400-555-017</p>
      </div>
      <footer class="back__footer">www.qorvel-insights.example</footer>
    </section>
  </main>
</body>
</html>
```